Skyreach e-Sport News site (skyreach.example).

The website will focus on news, results, fixtures, events, team news, upcoming events, team rankings etc. for the Tundrafox FPS game Skyreach (www.playskyreach.example). Site should have the same feel that has been already created by Tundrafox in the official site, with the blues and yellow hues and very graphical. Lots of content needed before the fold, similar sites include www.plexarion.example, www.na.quorbitleague.example, www.vantoplay.example, www.esports.drelvarion.example.

Target Market(s)

Gamers, males, 14-24.

Industry/Entity Type

Events

Font styles to use
Sans Serif
Other font styles liked:
• Big Noodle Titling for large headers.

Requirements
Must have
• A design closely resembling the theme already created by Tundrafox on their official site with use of in-game screenshots and vibrant colours through out.
• Focus on match results, fixtures and team rankings
Nice to have
• Ideal for full width grid layout

```html
<!DOCTYPE html>
<html lang="en">
<head>
<meta charset="utf-8">
<title>Skyreach E-Sports News</title>
<link rel="stylesheet" href="https://fonts.googleapis.com/css2?family=Bebas+Neue&family=Open+Sans:wght@400;600;700&display=swap">
<style>
:root{
  --navy:#08162c;
  --nav:#1677c4;
  --nav-dark:#0c3a68;
  --blue:#1b86cf;
  --blue-deep:#0f5c9e;
  --yellow:#f7c21b;
  --page:#d9e7f2;
  --white:#ffffff;
  --text:#4a5563;
  --muted:#8a94a3;
  --footer:#0f4f8a;
  --footer-dark:#082848;
  --line:#c8d6e3;
}
*{box-sizing:border-box;margin:0;padding:0}
html,body{width:1200px;height:2592px;overflow:hidden}
body{font-family:"Open Sans",Arial,sans-serif;color:var(--text);background:var(--page);font-size:13px;position:relative}
.display{font-family:"Bebas Neue",Impact,sans-serif;letter-spacing:1px}

/* header */
.topbar{height:120px;background:var(--navy);position:relative}
.brand{position:absolute;left:100px;top:38px;font-family:"Bebas Neue",Impact,sans-serif;font-size:46px;color:var(--yellow);letter-spacing:3px;display:flex;align-items:center;gap:12px}
.brand-dot{width:16px;height:16px;border-radius:50%;background:var(--yellow)}
.phone{position:absolute;left:780px;top:46px;display:flex;align-items:center;gap:12px;color:var(--white);font-size:20px}
.phone-icon{width:32px;height:32px;border:2px solid var(--white);border-radius:50%;display:flex;align-items:center;justify-content:center}
.login{position:absolute;left:990px;top:44px;width:110px;height:34px;background:var(--yellow);color:var(--navy);font-weight:700;font-size:14px;display:flex;align-items:center;justify-content:center;letter-spacing:1px}

.mainnav{height:44px;background:linear-gradient(#1d88d4,#1266ad);display:flex;padding-left:100px}
.mainnav a{color:var(--white);text-decoration:none;font-weight:600;font-size:14px;padding:0 17px;display:flex;align-items:center;border-right:1px solid rgba(255,255,255,.15)}
.mainnav a.active{background:var(--nav-dark)}

/* hero */
.hero{height:636px;position:relative;background:radial-gradient(circle at 30% 40%,#3a7fd8 0%,#16357a 40%,#081838 80%)}
.hero-caption{position:absolute;right:100px;top:360px;text-align:right;color:var(--white)}
.hero-caption h1{font-family:"Bebas Neue",Impact,sans-serif;font-size:76px;color:var(--yellow);letter-spacing:2px;line-height:1}
.hero-caption p{font-size:38px;font-weight:600;line-height:1.2}
.hero-arrow{position:absolute;top:300px;width:36px;height:36px;border-radius:50%;background:rgba(255,255,255,.25);display:flex;align-items:center;justify-content:center}
.hero-arrow.prev{left:16px}.hero-arrow.next{right:16px}

/* main */
.content{position:absolute;top:800px;left:100px;width:1000px;height:1460px}
.col-main{position:absolute;left:0;top:0;width:670px}
.col-side{position:absolute;left:700px;top:0;width:300px}
.section-head{display:flex;justify-content:space-between;align-items:center;height:40px;margin-top:12px;border-bottom:3px solid var(--blue)}
.section-head h2{font-family:"Bebas Neue",Impact,sans-serif;font-size:30px;color:var(--blue-deep);letter-spacing:1px}
.pager{display:flex;gap:6px}
.pager span{width:22px;height:22px;display:flex;align-items:center;justify-content:center}

.event-card{background:var(--white);border:1px solid var(--line);padding:12px;margin-top:14px;height:436px}
.event-media{height:232px;position:relative;background:linear-gradient(135deg,#2b3f6b,#6b7fa8 50%,#1d2c4e)}
.event-media.alt{background:linear-gradient(135deg,#a9b6c6,#e4d8c6 50%,#7c8ea6)}
.date-badge{position:absolute;left:14px;top:12px;width:56px;height:60px;background:var(--navy);color:var(--white);text-align:center;font-size:12px;padding-top:6px;line-height:1.2}
.date-badge b{display:block;font-size:22px}
.event-title{color:var(--blue);font-weight:700;font-size:13px;margin:16px 0 8px;text-transform:uppercase}
.event-text{font-size:12px;line-height:1.55}
.event-meta{font-size:11px;color:var(--muted);margin-top:14px}
.share-row{display:flex;justify-content:flex-end;gap:8px;border-top:1px solid var(--line);margin-top:14px;padding-top:10px}
.share-row span{font-size:11px;border:1px solid var(--line);border-radius:3px;padding:3px 10px;color:var(--blue-deep);background:#f2f6fa}

.results{display:flex;gap:24px;margin-top:18px}
.result-card{width:323px;height:300px;background:var(--white);border:1px solid var(--line);padding:10px}
.result-media{height:200px;background:linear-gradient(160deg,#2c5fb8,#0f2a68 60%,#4a7ad0)}
.result-media.alt{background:linear-gradient(160deg,#6a3bd0,#1b2f88 55%,#3a8fe0)}
.result-foot{display:flex;justify-content:space-between;align-items:center;margin-top:16px}
.result-foot p{font-size:12px;font-weight:700;color:var(--navy);text-transform:uppercase;line-height:1.5}
.circle-btn{width:30px;height:30px;border:1px solid var(--line);border-radius:50%;display:flex;align-items:center;justify-content:center;flex:none}

.fixtures-bar{margin-top:38px;height:80px;background:linear-gradient(90deg,#0b1a36,#1c3e75 60%,#0b1a36);display:flex;align-items:center;justify-content:space-between;padding:0 24px}
.fixtures-bar p{color:var(--white);font-size:14px;line-height:1.5;font-weight:600}
.fixtures-btn{background:var(--yellow);color:var(--navy);font-weight:700;padding:12px 26px;font-size:14px;letter-spacing:1px}

/* sidebar */
.panel{background:var(--white);border:1px solid var(--line);margin-top:12px}
.panel-head{height:44px;background:var(--blue);color:var(--white);font-weight:600;font-size:16px;display:flex;align-items:center;padding-left:14px}
.panel-body{padding:10px 14px}
.team-item{display:flex;gap:12px;padding:12px 0;border-bottom:1px solid #e4ebf2}
.team-item:last-child{border:none}
.thumb{width:84px;height:60px;flex:none;background:linear-gradient(135deg,#3a6bc4,#a9c3e8)}
.item-title{color:var(--blue);font-size:12px;font-weight:600;margin-bottom:4px}
.item-text{font-size:11px;line-height:1.45}
.upcoming{display:flex;gap:14px;padding:16px 0;border-bottom:1px solid #e4ebf2}
.upcoming:last-child{border:none}
.up-date{width:48px;height:52px;background:var(--blue-deep);color:var(--white);text-align:center;font-size:11px;padding-top:5px;flex:none;line-height:1.3}
.up-date b{display:block;font-size:18px}
.rank-row{display:flex;align-items:center;gap:10px;padding:7px 0;border-bottom:1px solid #eef2f6;font-size:12px}
.rank-row:last-child{border:none}
.flag{width:20px;height:13px;background:var(--muted)}
.rank-row .name{flex:1;color:var(--navy)}
.news-item{padding:12px 0;border-bottom:1px solid #e4ebf2}
.news-item:last-child{border:none}
.news-date{color:var(--blue);font-size:11px;font-weight:700;display:flex;align-items:center;gap:6px;margin-bottom:4px}

/* footer */
.footer{position:absolute;top:2260px;left:0;width:1200px;height:180px;background:var(--footer);display:flex;padding:30px 100px 0;gap:0}
.footer-col{width:250px}
.footer-col h3{color:var(--yellow);font-size:15px;font-weight:600;margin-bottom:10px}
.footer-col li{list-style:none;color:#c6dcf0;font-size:11px;line-height:1.75}
.subfooter{position:absolute;top:2440px;left:0;width:1200px;height:152px;background:var(--footer-dark);padding:28px 100px;color:#c6dcf0;font-size:12px}
.subfooter p{line-height:2}
.social{position:absolute;right:100px;top:30px;display:flex;gap:12px}
.social span{width:40px;height:40px;border-radius:50%;background:#2b6bb0}
</style>
</head>
<body>

<header class="topbar">
  <div class="brand"><span class="brand-dot"></span>SKYREACH</div>
  <div class="phone">
    <span class="phone-icon"><svg width="16" height="16" viewBox="0 0 24 24"><path fill="#fff" d="M6.6 10.8c1.4 2.8 3.8 5.1 6.6 6.6l2.2-2.2c.3-.3.7-.4 1-.2 1.1.4 2.3.6 3.6.6.6 0 1 .4 1 1V20c0 .6-.4 1-1 1C10.6 21 3 13.4 3 4c0-.6.4-1 1-1h3.5c.6 0 1 .4 1 1 0 1.3.2 2.5.6 3.6.1.3 0 .7-.2 1z"/></svg></span>
    555 014 2290
  </div>
  <div class="login">LOG IN</div>
</header>

<nav class="mainnav">
  <a class="active">HOME</a><a>SUBSCRIBER INFORMATION</a><a>RESULTS</a><a>ABOUT US</a><a>TEAM NEWS</a><a>FIXTURES</a><a>EVENTS</a><a>CONTACT US</a>
</nav>

<section class="hero" role="img" aria-label="Gamer with headset competing at a tournament in a blue-lit arena">
  <span class="hero-arrow prev"><svg width="12" height="12" viewBox="0 0 12 12"><path d="M8 1L3 6l5 5" stroke="#fff" stroke-width="2" fill="none"/></svg></span>
  <span class="hero-arrow next"><svg width="12" height="12" viewBox="0 0 12 12"><path d="M4 1l5 5-5 5" stroke="#fff" stroke-width="2" fill="none"/></svg></span>
  <div class="hero-caption">
    <h1>E-SPORTS NEWS</h1>
    <p>Lorem ipsum dolor sit amet<br>sectetur adipiscing elit</p>
  </div>
</section>

<main class="content">
  <div class="col-main">
    <div class="section-head"><h2>EVENTS</h2>
      <div class="pager"><span><svg width="10" height="12"><path d="M8 1L3 6l5 5" stroke="#0c3a68" stroke-width="2" fill="none"/></svg></span><span><svg width="10" height="12"><path d="M2 1l5 5-5 5" stroke="#0c3a68" stroke-width="2" fill="none"/></svg></span></div>
    </div>

    <article class="event-card">
      <div class="event-media" role="img" aria-label="Team of players competing at a tournament table">
        <div class="date-badge">Dec<b>20</b>2015</div>
      </div>
      <h3 class="event-title">Sectetur adipiscing elit, sed do eiusmod tempor incididunt</h3>
      <p class="event-text">Lorem ipsum has been the industry's standard dummy text ever since the 1500s, when an unknown printer took a galley of type and scrambled it to make a type specimen book. It has survived many centuries.</p>
      <p class="event-meta">This entry was posted in Newsdesk on 11/01/2015.</p>
      <div class="share-row"><span>Share</span><span>Like 1</span><span>Save 0</span></div>
    </article>

    <article class="event-card">
      <div class="event-media alt" role="img" aria-label="Group of friends celebrating at a gaming event">
        <div class="date-badge">Dec<b>20</b>2015</div>
      </div>
      <h3 class="event-title">Sectetur adipiscing elit, sed do eiusmod tempor incididunt</h3>
      <p class="event-text">Lorem ipsum has been the industry's standard dummy text ever since the 1500s, when an unknown printer took a galley of type and scrambled it to make a type specimen book. It has survived many centuries.</p>
      <p class="event-meta">This entry was posted in Newsdesk on 11/01/2015.</p>
      <div class="share-row"><span>Share</span><span>Like 1</span><span>Save 0</span></div>
    </article>

    <div class="section-head" style="margin-top:22px"><h2>RESULTS</h2>
      <div class="pager"><span><svg width="10" height="12"><path d="M8 1L3 6l5 5" stroke="#0c3a68" stroke-width="2" fill="none"/></svg></span><span><svg width="10" height="12"><path d="M2 1l5 5-5 5" stroke="#0c3a68" stroke-width="2" fill="none"/></svg></span></div>
    </div>
    <div class="results">
      <div class="result-card">
        <div class="result-media" role="img" aria-label="Tournament hall with rows of competing players"></div>
        <div class="result-foot"><p>Eiusmod tempor incididunt<br>ut labore et dolore</p><span class="circle-btn"><svg width="8" height="10"><path d="M2 1l4 4-4 4" stroke="#1b86cf" stroke-width="2" fill="none"/></svg></span></div>
      </div>
      <div class="result-card">
        <div class="result-media alt" role="img" aria-label="Arena stage with large screens and audience"></div>
        <div class="result-foot"><p>Eiusmod tempor incididunt<br>ut labore et dolore</p><span class="circle-btn"><svg width="8" height="10"><path d="M2 1l4 4-4 4" stroke="#1b86cf" stroke-width="2" fill="none"/></svg></span></div>
      </div>
    </div>
    <div class="fixtures-bar">
      <p>Lorem ipsum dolor sit amet, consectetur adipiscing elit, sed do<br>eiusmod tempor incididunt ut labore et dolore magna aliqua.</p>
      <span class="fixtures-btn">FIXTURES</span>
    </div>
  </div>

  <aside class="col-side">
    <div class="panel" style="height:336px">
      <div class="panel-head">Team News</div>
      <div class="panel-body">
        <div class="team-item"><div class="thumb" role="img" aria-label="Team photo"></div><div><p class="item-title">Sectetur adipiscing</p><p class="item-text">Lorem ipsum dolor sit amet, consectetur elit sed do.</p></div></div>
        <div class="team-item"><div class="thumb" role="img" aria-label="Team photo"></div><div><p class="item-title">Sectetur adipiscing</p><p class="item-text">Lorem ipsum dolor sit amet, consectetur elit sed do.</p></div></div>
        <div class="team-item"><div class="thumb" role="img" aria-label="Team photo"></div><div><p class="item-title">Sectetur adipiscing</p><p class="item-text">Lorem ipsum dolor sit amet, consectetur elit sed do.</p></div></div>
      </div>
    </div>

    <div class="panel" style="height:336px;margin-top:28px">
      <div class="panel-head">Upcoming Events</div>
      <div class="panel-body">
        <div class="upcoming"><div class="up-date">Dec<b>18</b>Sat</div><p class="item-text">Ipsum dolor sit amet sectetur adipiscing elit. Sed do eiusmod tempor incididunt ut labore.</p></div>
        <div class="upcoming"><div class="up-date">Dec<b>19</b>Sun</div><p class="item-text">Ipsum dolor sit amet sectetur adipiscing elit. Sed do eiusmod tempor incididunt ut labore.</p></div>
        <div class="upcoming"><div class="up-date">Dec<b>20</b>Mon</div><p class="item-text">Ipsum dolor sit amet sectetur adipiscing elit. Sed do eiusmod tempor incididunt ut labore.</p></div>
      </div>
    </div>

    <div class="panel" style="height:340px;margin-top:24px">
      <div class="panel-head">Team Rankings</div>
      <div class="panel-body">
        <div class="rank-row"><span class="flag"></span><span class="name">Korvex Squad</span>11,821</div>
        <div class="rank-row"><span class="flag"></span><span class="name">Nimbra Five</span>11,383</div>
        <div class="rank-row"><span class="flag"></span><span class="name">Tessar Unit</span>7,447</div>
        <div class="rank-row"><span class="flag"></span><span class="name">Frostgard</span>5,198</div>
        <div class="rank-row"><span class="flag"></span><span class="name">Dravenhollow</span>3,891</div>
        <div class="rank-row"><span class="flag"></span><span class="name">Pulsewire</span>3,248</div>
        <div class="rank-row"><span class="flag"></span><span class="name">Orbitlane</span>3,105</div>
        <div class="rank-row"><span class="flag"></span><span class="name">Vesta Rising</span>2,987</div>
      </div>
    </div>

    <div class="panel" style="height:292px;margin-top:24px">
      <div class="panel-head">News</div>
      <div class="panel-body">
        <div class="news-item"><p class="news-date"><svg width="10" height="10"><circle cx="5" cy="5" r="4" fill="#1b86cf"/></svg>DEC 19, 2015</p><p class="item-text">Lorem ipsum dolor sit amet, consectetur adipiscing elit, sed do eiusmod tempor incididunt ut labore et dolore.</p></div>
        <div class="news-item"><p class="news-date"><svg width="10" height="10"><circle cx="5" cy="5" r="4" fill="#1b86cf"/></svg>DEC 19, 2015</p><p class="item-text">Lorem ipsum dolor sit amet, consectetur adipiscing elit, sed do eiusmod tempor incididunt ut labore et dolore.</p></div>
      </div>
    </div>
  </aside>
</main>

<footer class="footer">
  <div class="footer-col"><h3>How We Help</h3><ul><li>Lead Generation</li><li>Tutorial Management</li><li>Event Ops Network</li><li>Website Handlers</li></ul></div>
  <div class="footer-col"><h3>Services</h3><ul><li>Search Match Reporting</li><li>Website Analysis</li><li>League Media Design</li><li>Broadcasting</li></ul></div>
  <div class="footer-col"><h3>Results</h3><ul><li>Construction</li><li>Bulk Engagement</li><li>Fixtures and Tournaments</li><li>Manufacturing</li></ul></div>
  <div class="footer-col"><h3>Support</h3><ul><li>Member Handbook</li><li>Live Chat Service</li><li>Our Team</li><li>Sitemap</li></ul></div>
</footer>

<div class="subfooter">
  <p>Privacy Policy | Terms of Use | About Us | Sitemap</p>
  <p>Copyright © 2015 Skyreach. All rights reserved.</p>
  <div class="social"><span></span><span></span><span></span><span></span></div>
</div>

</body>
</html>
```